Help develop the "Steady Brew" Logo & Can Design for new beer!

We're a new beer being produced in the Caribbean. Thus looking for a beer logo design that
1) capitalizes on the word "Steady" for further beer lines that spin off of this first one. EXAMPLES OF OTHER BEER NAMES TO BE PRODUCED THAT HAVE TO HAVE TIE IN TO ORIGINAL DESIGN: "One Steady Brew", "My Cousins Tamarind Brew" "Pelicane Steady Brew" "Wha gwan now Steady Brew" "De hour for Steady Brew", "Sorrelo Steady Brew" etc etc etc,

2) has unique visual impact,
3) Logo has to be usable across variety of mediums,
4) 4 color maximum,
5) Island art feel,
6) Steady Brew needs to convey a since of "lightness and slight tongue-in-cheek or off beat humor"...but not overwhelming,
7) Each subsequent label names (see above) needs to be distinctly color coded, but connects to the overarching theme of the brand with distinctive interpretations of each beer’s name.
8) Needs to be BOLD in statement and color.

You can get inspiration from some of these logo's. Follow this link: http://www.quillmarkstudio.example/retro-marks/
or http://www.boxandlabelgallery.example/2014/12/30-brews-for-30-seasons-2001-to-2006.html

Also see attached files for inspiration!!!

Reason: We've extended the deadline for this project! Thus submit any new designs sooner than later. Thanks!

Target Market(s)

Male: Wear jeans & baseball cap, Played H.S. sports, Hunts/fish/golfDrive a truck or SUV, Work a blue collar job, Like working in the garage or on the landLike football/basketball/baseball, Are married high school sweetheart and have childrenAre from southern states...or wished they were, Chews tobacco or smokeDrink beerFemale: Attended college/community collegeAre married with kidsRide motorcycles, 4x4, ATV’sDrive Trucks or vansFish/camp/garden/sewDo craftsDrink beerGets manicures/pedicuresWears jewelry & jeans

Logo Text

Steady Brew

Logo styles of interest
Emblem Logo
Pictorial/Combination Logo
Abstract Logo
Character Logo
Wordmark Logo
Requirements
Must have
• Eye catching & readable shelf presentation. Non-Standard art. High definition. Bold Statement. Clear design elements, various color options, High color contrast (like attached files) are needed for visual impact. Simple elements that conveys essence of the brand.
• You are designing the whole "beer can" logo elements, not just the the main logo. Things like background and side panels. Back panel for ingredients and messages to be added to. This is an "overall" can design, not just a single logo design.
• MUST HAVE THESE WORDS/SENTENCES/SECTIONS:
• Sentences: Our Steady ales and lagers are handcrafted with some of the best ingredients the Caribbean has to offer!
• Section: So, Why Do we use can's?
• Can's eliminate potential light damage, reduce the risk of oxidation are lighter and chill quicker. Can be enjoyed on beaches and make for great recycling and table art. Plus they are the most recycled and eco-friendly material we can use. Steady!
• BREWED AND BOTTLED/PACKED BY:
• IMPORTED BY
• ALCOHOL (ALC) ______% BY VOLUME (VOL)
• Recyclable
• GOVERNMENT WARNING:
• (1) According to the Surgeon General, women should not drink alcoholic beverages during pregnancy because of the risk of birth defects. (2) Consumption of
• alcoholic beverages impairs your ability to drive a car or operate machinery, and may cause health problems.
• Description: (This will change from beer to beer but this is good example of type language we would be using. "This Steady Brew has a pletheria of Island goodness (there are hints of passion fruit, mango, and pineapple) along with some pleasant bitterness IPAs are known for. We can honestly say these sweet and savory flavors pair perfectly with this beer and you'll get a kick out of the IPA notes too!"
Should not have
• nudity, graphic language, skulls, flames,

```html
<!DOCTYPE html>
<html lang="en">
<head>
<meta charset="utf-8">
<title>Steady Brew – Can Range</title>
<link rel="stylesheet" href="https://fonts.googleapis.com/css2?family=Bungee&family=Rye&family=Roboto:ital,wght@0,400;0,700;0,900;1,700&display=swap">
<style>
  :root {
    --paper: #ffffff;
    --band-red: #e8401f;
    --band-line: #f47a5a;
    --gold: #f5b21a;
    --ink: #141414;
    --steel-light: #f2f2f2;
    --steel-mid: #b9b9b9;
    --steel-dark: #7d7d7d;
    --face: #ffffff;
    --extrude: #b7b7b7;
    --extrude-dark: #8e8e8e;
    --sea: #c6e8ef;
    --sea-deep: #b3dfe9;
    --map-red: #e3301f;
    --map-soft: #f2b3a8;
    --mark-orange: #f39a1b;
    --can-sorrelo: #f8d90f;
    --can-pelicane: #ea5a22;
    --can-tamarind: #f49d1c;
    --can-whagwan: #e3321f;
    --can-dehour: #f2ae16;
  }
  * { box-sizing: border-box; margin: 0; padding: 0; }
  html, body { width: 1200px; height: 1000px; overflow: hidden; background: var(--paper); }
  .board { position: relative; width: 1200px; height: 1000px; overflow: hidden; background: var(--paper); font-family: "Roboto", Arial, sans-serif; }

  /* brand mark */
  .brand-mark { position: absolute; left: 28px; top: 32px; width: 140px; text-align: center; color: var(--mark-orange); }
  .brand-mark__dot { display: block; width: 54px; height: 54px; margin: 0 auto 10px; border-radius: 50%; background: var(--mark-orange); }
  .brand-mark__name { font-weight: 700; font-size: 14px; letter-spacing: .5px; }

  /* diagonal band */
  .hero-band { position: absolute; left: 0; top: 0; width: 1200px; height: 520px; }

  /* banner wordmark */
  .hero-word {
    position: absolute; left: 236px; top: 196px; width: 760px;
    font-family: "Bungee", Impact, sans-serif; font-size: 188px; line-height: 1; letter-spacing: -4px;
    color: var(--face);
    -webkit-text-stroke: 4px var(--ink);
    text-shadow:
      -2px 2px 0 var(--extrude), -4px 4px 0 var(--extrude), -6px 6px 0 var(--extrude),
      -8px 8px 0 var(--extrude-dark), -10px 10px 0 var(--extrude-dark),
      -13px 13px 0 var(--gold), -16px 16px 0 var(--ink),
      0 0 30px rgba(255,255,255,.55);
    transform: skewY(-14.5deg); transform-origin: 0 50%;
  }
  .hero-tag {
    position: absolute; left: 497px; top: 352px; width: 210px; height: 92px;
    background: var(--gold);
    transform: skewY(-14.5deg); transform-origin: 0 50%;
    display: flex; align-items: center; justify-content: center;
    border-top: 3px solid var(--band-red); border-bottom: 3px solid var(--band-red);
    outline: 6px solid var(--gold);
  }
  .hero-tag__word {
    font-family: "Bungee", Impact, sans-serif; font-size: 66px; line-height: 1; color: var(--face);
    -webkit-text-stroke: 2px var(--band-red);
    text-shadow: -3px 3px 0 var(--extrude), -5px 5px 0 var(--band-red);
  }

  /* cans */
  .can { position: absolute; top: 518px; width: 222px; height: 432px; }
  .can__lid {
    position: absolute; left: 6px; right: 6px; top: 0; height: 26px; border-radius: 50% / 40%;
    background: linear-gradient(90deg, var(--steel-dark), var(--steel-light) 30%, var(--steel-mid) 60%, var(--steel-light) 80%, var(--steel-dark));
  }
  .can__body { position: absolute; left: 0; right: 0; top: 22px; height: 346px; overflow: hidden; background: var(--can-color); }
  .can__sea { position: absolute; left: 0; right: 0; top: 160px; bottom: 0;
    background: linear-gradient(180deg, var(--sea), var(--sea-deep));
    clip-path: polygon(0 34px, 100% 0, 100% 100%, 0 100%); }
  .can__side-note { position: absolute; left: 2px; top: 54px; font-size: 6px; line-height: 8px; font-weight: 700; color: var(--ink); }
  .can__mark { position: absolute; left: 0; right: 0; top: 60px; text-align: center; }
  .can__mark-dot { display: block; width: 24px; height: 24px; margin: 0 auto 5px; border-radius: 50%; background: var(--face); }
  .can__mark-name { font-weight: 700; font-size: 8px; color: var(--face); letter-spacing: .3px; }
  .can__ribbon {
    position: absolute; left: 50%; top: 124px; transform: translateX(-50%) rotate(-5deg);
    padding: 2px 12px; background: var(--face); border-left: 8px solid var(--map-red); border-right: 8px solid var(--map-red);
    font-family: "Rye", Georgia, serif; font-size: 10px; line-height: 12px; color: var(--ink); white-space: nowrap;
  }
  .can__name {
    position: absolute; left: 0; right: 0; top: 146px; text-align: center;
    font-family: "Bungee", Impact, sans-serif; font-size: 45px; line-height: 1; letter-spacing: -1.5px; color: var(--face);
    -webkit-text-stroke: 1.5px var(--ink);
    text-shadow: -2px 2px 0 var(--extrude), -3px 3px 0 var(--extrude-dark), -5px 5px 0 var(--ink);
  }
  .can__brew {
    position: absolute; left: 50%; top: 202px; transform: translateX(-50%) rotate(-4deg);
    padding: 2px 8px; background: var(--tag-color);
    font-family: "Bungee", Impact, sans-serif; font-size: 20px; line-height: 1; color: var(--face);
    -webkit-text-stroke: 1px var(--map-red);
  }
  .can__map { position: absolute; left: 74px; top: 240px; width: 74px; height: 66px; border-radius: 6px;
    background: linear-gradient(160deg, var(--map-soft), var(--sea-deep)); }
  .can__strip { position: absolute; left: 0; right: 0; top: 314px; height: 18px; background: var(--ink);
    color: var(--face); font-size: 8.5px; line-height: 18px; white-space: nowrap; padding-left: 4px; }
  .can__strip b { font-weight: 900; }
  .can__shade { position: absolute; inset: 0;
    background: linear-gradient(90deg, rgba(0,0,0,.18), rgba(255,255,255,.12) 28%, rgba(255,255,255,0) 45%, rgba(0,0,0,.05) 75%, rgba(0,0,0,.2)); }
  .can__base {
    position: absolute; left: 2px; right: 2px; top: 366px; height: 66px; border-radius: 0 0 50% 50% / 0 0 30% 30%;
    background: linear-gradient(90deg, var(--steel-dark), var(--steel-light) 25%, var(--steel-mid) 55%, var(--steel-light) 78%, var(--steel-dark));
  }

  .can--sorrelo  { left: 25px;  --can-color: var(--can-sorrelo);  --tag-color: var(--can-pelicane); }
  .can--pelicane { left: 258px; --can-color: var(--can-pelicane); --tag-color: var(--mark-orange); }
  .can--tamarind { left: 490px; --can-color: var(--can-tamarind); --tag-color: var(--can-whagwan); }
  .can--whagwan  { left: 723px; --can-color: var(--can-whagwan);  --tag-color: var(--mark-orange); }
  .can--dehour   { left: 955px; --can-color: var(--can-dehour);   --tag-color: var(--can-whagwan); }
</style>
</head>
<body>
<main class="board">

  <div class="brand-mark">
    <span class="brand-mark__dot"></span>
    <span class="brand-mark__name">LAS CORALINAS</span>
  </div>

  <svg class="hero-band" viewBox="0 0 1200 520" aria-hidden="true">
    <defs>
      <pattern id="band-stripes" patternUnits="userSpaceOnUse" width="40" height="14" patternTransform="rotate(-14.5)">
        <rect width="40" height="14" fill="var(--band-red)"/>
        <rect y="12" width="40" height="1.2" fill="var(--band-line)"/>
      </pattern>
    </defs>
    <line x1="0" y1="183" x2="1200" y2="-127" stroke="var(--band-red)" stroke-width="2"/>
    <polygon points="0,200 1200,-110 1200,150 0,460" fill="url(#band-stripes)"/>
    <line x1="0" y1="209" x2="1200" y2="-101" stroke="var(--paper)" stroke-width="2"/>
    <line x1="0" y1="450" x2="1200" y2="140" stroke="var(--paper)" stroke-width="2"/>
    <line x1="0" y1="475" x2="1200" y2="165" stroke="var(--band-red)" stroke-width="2"/>
    <line x1="0" y1="492" x2="1200" y2="182" stroke="var(--band-red)" stroke-width="1.5"/>
  </svg>

  <h1 class="hero-word">STEADY</h1>
  <div class="hero-tag"><span class="hero-tag__word">BREW</span></div>

  <section class="can-range">
    <article class="can can--sorrelo">
      <div class="can__lid"></div>
      <div class="can__body">
        <div class="can__sea" role="img" aria-label="Island sea pattern"></div>
        <p class="can__side-note">chill quicker.<br>great<br>table art.<br>friendly</p>
        <div class="can__mark"><span class="can__mark-dot"></span><span class="can__mark-name">LAS CORALINAS</span></div>
        <div class="can__name">STEADY</div>
        <div class="can__ribbon">Sorrelo</div>
        <div class="can__brew">BREW</div>
        <div class="can__map" role="img" aria-label="Map of the islands"></div>
        <div class="can__strip"><b>Lagers</b> are <b><i>handcrafted</i></b> with some of the best ingredients the C</div>
        <div class="can__shade"></div>
      </div>
      <div class="can__base"></div>
    </article>

    <article class="can can--pelicane">
      <div class="can__lid"></div>
      <div class="can__body">
        <div class="can__sea" role="img" aria-label="Island sea pattern"></div>
        <p class="can__side-note">chill quicker.<br>great<br>table art.<br>friendly</p>
        <div class="can__mark"><span class="can__mark-dot"></span><span class="can__mark-name">LAS CORALINAS</span></div>
        <div class="can__name">STEADY</div>
        <div class="can__ribbon">Pelicane</div>
        <div class="can__brew">BREW</div>
        <div class="can__map" role="img" aria-label="Map of the islands"></div>
        <div class="can__strip"><b>Lagers</b> are <b><i>handcrafted</i></b> with some of the best ingredients the C</div>
        <div class="can__shade"></div>
      </div>
      <div class="can__base"></div>
    </article>

    <article class="can can--tamarind">
      <div class="can__lid"></div>
      <div class="can__body">
        <div class="can__sea" role="img" aria-label="Island sea pattern"></div>
        <p class="can__side-note">chill quicker.<br>great<br>table art.<br>friendly</p>
        <div class="can__mark"><span class="can__mark-dot"></span><span class="can__mark-name">LAS CORALINAS</span></div>
        <div class="can__name">STEADY</div>
        <div class="can__ribbon">My Cousins Tamarind</div>
        <div class="can__brew">BREW</div>
        <div class="can__map" role="img" aria-label="Map of the islands"></div>
        <div class="can__strip"><b>Lagers</b> are <b><i>handcrafted</i></b> with some of the best ingredients the C</div>
        <div class="can__shade"></div>
      </div>
      <div class="can__base"></div>
    </article>

    <article class="can can--whagwan">
      <div class="can__lid"></div>
      <div class="can__body">
        <div class="can__sea" role="img" aria-label="Island sea pattern"></div>
        <p class="can__side-note">chill quicker.<br>great<br>table art.<br>friendly</p>
        <div class="can__mark"><span class="can__mark-dot"></span><span class="can__mark-name">LAS CORALINAS</span></div>
        <div class="can__name">STEADY</div>
        <div class="can__ribbon">Wha gwan now</div>
        <div class="can__brew">BREW</div>
        <div class="can__map" role="img" aria-label="Map of the islands"></div>
        <div class="can__strip"><b>Lagers</b> are <b><i>handcrafted</i></b> with some of the best ingredients the C</div>
        <div class="can__shade"></div>
      </div>
      <div class="can__base"></div>
    </article>

    <article class="can can--dehour">
      <div class="can__lid"></div>
      <div class="can__body">
        <div class="can__sea" role="img" aria-label="Island sea pattern"></div>
        <p class="can__side-note">chill quicker.<br>great<br>table art.<br>friendly</p>
        <div class="can__mark"><span class="can__mark-dot"></span><span class="can__mark-name">LAS CORALINAS</span></div>
        <div class="can__name">STEADY</div>
        <div class="can__ribbon">DE HOUR FOR</div>
        <div class="can__brew">BREW</div>
        <div class="can__map" role="img" aria-label="Map of the islands"></div>
        <div class="can__strip"><b>Lagers</b> are <b><i>handcrafted</i></b> with some of the best ingredients the C</div>
        <div class="can__shade"></div>
      </div>
      <div class="can__base"></div>
    </article>
  </section>

</main>
</body>
</html>
```